Varnel Group Business Card design with current logo

hello all , we have abranded logo which i will attach but we need a card double sided designed . one side is easy as its the logo but the other side we want clean and modern. The info needed will be the same text as the card sample attached. no pictures of us though just clean and professinal pls. Logo can be incorporated on the text side to for recognition. Colors are Black , white , red and grey... ideal card would be matt finish high end stock. or a black card so white text ... Sorry i have uploaded al the files i got when I had the logo designed on here.. Oh forgot want to say pls add in the card details EST 1981 and over 40yrs combined experiance
Updates

Hello everyone , I'm really sorry we haven't been able to make a final decision.. There is at least 3 cards that all have there positives over the other two... We will decide by tonight.

Target Market(s)

20-70 wide range but people with money and a education.

Industry/Entity Type

Real Estate Agent

Contact Information for Business Card

One side the Logo choose from the different color logos, black being the one we like most, other side is the details. Clean professional looking fonts. EST 1981 , over 40yrs experiance. Website email and both names and PH# as per the sample card attached

Font styles to use
Other font styles liked:
• Fonts:Code Bold,Code Light, Lucida Fax.

Colors
1b1b1b
757575
c9c9c9
e8e8e8
ffffff
e9e9e9

Requirements
Must have
• Logo and contact info

```html
<!DOCTYPE html>
<html lang="en">
<head>
<meta charset="utf-8">
<title>Varnel Group Business Card</title>
<link href="https://fonts.googleapis.com/css2?family=Cinzel:wght@400;600&family=Questrial&display=swap" rel="stylesheet">
<style>
  :root {
    --ink: #1b1b1b;
    --charcoal: #2e2e2e;
    --grey: #757575;
    --silver: #b4b4b4;
    --light: #c9c9c9;
    --paper: #ffffff;
    --backdrop: #e8e8e8;
    --red: #c1272d;
  }
  html, body { margin: 0; padding: 0; overflow: hidden; }
  body {
    width: 1200px; height: 1100px; position: relative;
    background: var(--backdrop);
    font-family: "Cinzel", serif;
  }
  .card { position: absolute; left: 220px; width: 755px; height: 443px; overflow: hidden; }

  /* Front */
  .card-front {
    top: 100px;
    background: radial-gradient(ellipse 300px 230px at 52% 48%, #5a5a5a 0%, #2d2d2d 65%, var(--ink) 100%);
  }
  .card-front .fold { position: absolute; right: 0; top: 0; width: 82px; height: 100%; background: var(--ink); border-left: 1px solid #333; }
  .brand { position: absolute; display: flex; align-items: center; }
  .brand-square { background: var(--silver); }
  .brand-name { color: var(--silver); font-family: "Questrial", sans-serif; letter-spacing: 2px; line-height: 1; }
  .card-front .brand { left: 225px; top: 148px; }
  .card-front .brand-square { width: 127px; height: 127px; }
  .card-front .brand-name { font-size: 52px; margin-left: 18px; }

  /* Back */
  .card-back { top: 563px; background: var(--paper); }
  .card-back svg.swoosh { position: absolute; left: 0; top: 0; }
  .card-back .brand { left: 52px; top: 40px; }
  .card-back .brand-square { width: 103px; height: 97px; }
  .card-back .brand-name { font-size: 40px; margin-left: 14px; }
  .est { position: absolute; left: 53px; top: 150px; color: var(--light); font-size: 15px; letter-spacing: 1px; }

  .agents { position: absolute; right: 57px; top: 200px; text-align: right; }
  .agent { color: var(--ink); font-size: 38px; line-height: 1; margin: 0; letter-spacing: 0.5px; }
  .experience {
    position: absolute; right: 0; top: 237px; width: 348px; height: 19px;
    background: var(--red); color: var(--paper);
    font-size: 14.5px; font-weight: 600; line-height: 19px; text-align: center; letter-spacing: 0.5px;
  }
  .agent-second { position: absolute; right: 57px; top: 258px; }
  .contact { position: absolute; right: 57px; top: 308px; text-align: right; color: #333; font-size: 15px; line-height: 19px; letter-spacing: 0.5px; }

  .office { position: absolute; left: 54px; top: 267px; }
  .office-mark { display: flex; align-items: center; }
  .office-mark .brand-square { width: 14px; height: 14px; background: var(--red); margin-right: 8px; }
  .office-name { color: var(--ink); font-size: 17px; font-weight: 600; }
  .office-sub { color: #333; font-size: 12px; margin-top: 4px; font-family: "Questrial", sans-serif; }
  .address { position: absolute; left: 55px; top: 343px; color: #333; font-size: 15px; line-height: 19px; letter-spacing: 0.5px; }
</style>
</head>
<body>
  <section class="card card-front">
    <div class="brand">
      <div class="brand-square"></div>
      <span class="brand-name">VARNEL GROUP</span>
    </div>
    <div class="fold"></div>
  </section>

  <section class="card card-back">
    <svg class="swoosh" width="755" height="443" viewBox="0 0 755 443" aria-hidden="true">
      <defs>
        <radialGradient id="brandGlow" cx="0.2" cy="0.2" r="0.5">
          <stop offset="0" stop-color="#4a4a4a"/>
          <stop offset="1" stop-color="#2e2e2e"/>
        </radialGradient>
      </defs>
      <rect width="755" height="443" fill="url(#brandGlow)"/>
      <path d="M0,215 Q310,140 755,150 L755,160 Q310,152 0,226 Z" fill="#ffffff"/>
      <path d="M0,226 Q310,152 755,160 L755,178 Q330,168 0,282 Z" fill="#c1272d"/>
      <path d="M0,282 Q330,168 755,178 L755,443 L0,443 Z" fill="#ffffff"/>
    </svg>

    <div class="brand">
      <div class="brand-square"></div>
      <span class="brand-name">VARNEL GROUP</span>
    </div>
    <div class="est">EST 1981</div>

    <div class="agents"><p class="agent">Don Varnel</p></div>
    <div class="experience">OVER 40 YRS COMBINED EXPERIENCE</div>
    <p class="agent agent-second">Jordan Varnel</p>

    <div class="contact">
      Phone: 250-555-0142<br>
      Fax: 250-555-0187<br>
      Email: info@VarnelRealEstate.com<br>
      Web: www.VarnelRealEstate.com
    </div>

    <div class="office">
      <div class="office-mark"><div class="brand-square"></div><span class="office-name">HARBOUR CREST</span></div>
      <div class="office-sub">Shoreline Realty</div>
    </div>
    <div class="address">
      Harbour Crest Shoreline<br>
      210-3875 Marlow Way<br>
      Victoria BC V8Z4K1
    </div>
  </section>
</body>
</html>
```